New website design for tech company

I want to redesign the current website - https://quorvalent.co/
I want it to keep the same colors/branding but I want it to resemble the look and feel of the following sites
https://www.drelkusa.com/
https://www.munoro.com/
https://www.pulvane.com/global/us/home
https://www.tovinplc.co.uk/

The site layout

Target Market(s)

tech companies

Industry/Entity Type

tech

Number of Pages Required

2 page

Font styles to use
Serif

Colors

Designer to choose colors to be used in the design.

Requirements
Must have
• a nice updated design that looks cutting edge and innovative and the site colors can match the current logo

```html
<!DOCTYPE html>
<html lang="en">
<head>
<meta charset="utf-8">
<title>Quorvalent — Accessible Web Technology</title>
<link rel="stylesheet" href="https://fonts.googleapis.com/css2?family=Outfit:wght@300;400;500;600;700&display=swap">
<style>
:root{
  --blue:#0b57a8;
  --blue-dark:#08427f;
  --green:#8dc63f;
  --green-soft:#e6f2d6;
  --ink:#1c1c1c;
  --muted:#444;
  --hero-a:#1f3a45;
  --hero-b:#4c6670;
  --grey:#efefef;
  --footer-bar:#1d1d1d;
}
*{box-sizing:border-box;margin:0;padding:0}
html,body{width:1200px;height:3995px;overflow:hidden}
body{font-family:"Outfit",sans-serif;color:var(--ink);background:#fff;position:relative}
.abs{position:absolute}
.btn{position:absolute;display:flex;align-items:center;justify-content:space-between;background:var(--blue);color:#fff;border-radius:30px;font-size:13px;padding:0 5px 0 20px;height:44px}
.btn .arrow{width:34px;height:34px;border-radius:50%;background:#fff;display:flex;align-items:center;justify-content:center}
.btn.light{background:#fff;color:var(--blue)}
.btn.light .arrow{background:var(--blue)}
.title{position:absolute;left:0;width:1200px;text-align:center;font-size:36px;font-weight:500;color:var(--blue)}
.title .g,.g{color:var(--green)}
.logo-word{font-weight:700;font-size:30px;color:var(--green);letter-spacing:1px;display:flex;align-items:center;gap:10px}
.logo-word .dot{width:22px;height:22px;border-radius:50%;background:var(--blue)}
/* header */
.topbar{height:88px}
.contact-item{position:absolute;top:26px;display:flex;align-items:center;gap:10px;font-size:12px;line-height:1.3}
.contact-item .ic{width:28px;height:28px;border-radius:50%;background:var(--green);display:flex;align-items:center;justify-content:center}
.nav{position:absolute;top:88px;left:0;width:1200px;height:48px;background:var(--blue);display:flex;padding:0 140px}
.nav a{flex:1;color:#fff;font-size:13px;text-align:center;line-height:48px;text-decoration:none;border-right:1px solid rgba(255,255,255,.18)}
.nav a:last-child{border:0}
/* hero */
.hero{position:absolute;top:136px;left:0;width:1200px;height:560px;background:linear-gradient(90deg,var(--hero-a),var(--hero-b));overflow:hidden}
.hero-visual{position:absolute;right:0;top:0;width:640px;height:560px;background:linear-gradient(135deg,#5a7d8a,#2b4f63 55%,#17344a)}
.hero h1{position:absolute;left:140px;top:158px;width:470px;font-size:35px;font-weight:500;color:#fff;line-height:1.27}
.hero .kicker{position:absolute;left:140px;top:120px;color:var(--green);font-size:19px}
.hero .tag{position:absolute;left:140px;top:305px;color:var(--green);font-size:19px}
.p-center{position:absolute;left:160px;width:880px;text-align:center;font-size:17px;line-height:1.65;color:var(--ink)}
/* about */
.about-img{position:absolute;left:165px;top:1033px;width:395px;height:425px;border-radius:48% 52% 45% 55%/35% 45% 55% 65%;background:linear-gradient(135deg,#6c7c86,#b8c3c6 55%,#d5dadb)}
.about-blob{position:absolute;left:142px;top:1060px;width:415px;height:415px;border-radius:50%;background:var(--green-soft)}
.about-text{position:absolute;left:608px;width:450px;font-size:13.5px;line-height:1.95;color:var(--muted)}
/* services */
.card{position:absolute;top:1627px;width:290px;height:313px;background:#fff;border:1px solid #e7e7e7;border-radius:6px;box-shadow:0 3px 12px rgba(0,0,0,.07);text-align:center}
.card .icon{width:84px;height:84px;border-radius:50%;background:var(--green);margin:27px auto 0;display:flex;align-items:center;justify-content:center}
.card h3{font-size:18px;font-weight:400;margin-top:22px;line-height:1.35}
.card p{font-size:12px;line-height:1.85;color:var(--muted);margin:14px 22px 0}
.card .more{font-size:12.5px;color:var(--blue);margin-top:14px}
/* reviews */
.client{position:absolute;width:200px;height:200px;border-radius:50%;background:#fff;box-shadow:0 4px 18px rgba(0,0,0,.1);display:flex;flex-direction:column;align-items:center;justify-content:center;gap:8px;font-weight:700;font-size:12px}
.client .mark{width:40px;height:40px;border-radius:50%}
/* serve */
.serve{position:absolute;left:140px;top:2527px;width:920px;height:273px;border-radius:22px;overflow:hidden;background:var(--green)}
.serve-visual{position:absolute;right:0;top:0;width:480px;height:273px;background:linear-gradient(135deg,#0b2a5a,#1a5fa8 50%,#0b1a3a)}
/* blog */
.post{position:absolute;top:2948px;width:280px;height:364px;background:#fff;box-shadow:0 2px 12px rgba(0,0,0,.09);padding:8px}
.post .thumb{height:200px;position:relative}
.post .date{position:absolute;left:10px;top:-8px;width:50px;height:50px;background:var(--blue);color:#fff;text-align:center;font-size:11px;line-height:1.1;padding-top:6px}
.post .date b{display:block;font-size:17px;font-weight:500}
.post h4{font-size:12.5px;font-weight:600;margin:18px 8px 0;line-height:1.45}
.post p{font-size:11px;line-height:1.7;color:var(--muted);margin:4px 8px 0}
.post .more{font-size:11px;color:var(--blue);margin:8px 8px 0}
.side-arrow{position:absolute;top:3108px;width:44px;height:44px;border-radius:50%;display:flex;align-items:center;justify-content:center}
/* newsletter */
.grey-band{position:absolute;left:0;top:3630px;width:1200px;height:323px;background:var(--grey)}
.news{position:absolute;left:140px;top:3467px;width:920px;height:236px;background:var(--blue);border-radius:6px;color:#fff;text-align:center}
.field{position:absolute;top:3620px;width:200px;height:40px;background:#fff;border-radius:22px;font-size:12px;color:#555;padding-left:18px;line-height:40px}
/* footer */
.fhead{position:absolute;top:3755px;font-size:15px;font-weight:500;color:var(--blue)}
.flist{position:absolute;font-size:12.5px;line-height:21.5px}
.fic{width:28px;height:28px;border-radius:50%;border:1.5px solid var(--blue);display:inline-flex;align-items:center;justify-content:center;flex:none}
.frow{position:absolute;display:flex;gap:12px;align-items:flex-start;font-size:12.5px;line-height:1.55}
.bottom{position:absolute;left:0;top:3953px;width:1200px;height:42px;background:var(--footer-bar);color:#ddd;font-size:11.5px;display:flex;justify-content:space-between;align-items:center;padding:0 140px}
</style>
</head>
<body>

<!-- Header -->
<header class="topbar">
  <div class="abs logo-word" style="left:140px;top:24px">QUORVALENT<span class="dot"></span></div>
  <div class="contact-item" style="left:515px">
    <span class="ic"><svg width="14" height="14" viewBox="0 0 24 24"><path fill="#fff" d="M6.6 10.8a15 15 0 0 0 6.6 6.6l2.2-2.2a1 1 0 0 1 1-.25 11 11 0 0 0 3.6.6 1 1 0 0 1 1 1V20a1 1 0 0 1-1 1A17 17 0 0 1 3 4a1 1 0 0 1 1-1h3.5a1 1 0 0 1 1 1c0 1.25.2 2.45.6 3.6a1 1 0 0 1-.25 1z"/></svg></span>
    <span>Phone<br>123 456 7890</span>
  </div>
  <div class="contact-item" style="left:655px">
    <span class="ic"><svg width="14" height="14" viewBox="0 0 24 24"><path fill="#fff" d="M3 5h18v14H3z"/><path d="M3 5l9 7 9-7" stroke="#8dc63f" stroke-width="2" fill="none"/></svg></span>
    <span>Email<br>inquiry@quorvalent.com</span>
  </div>
  <div class="btn" style="left:846px;top:25px;width:213px;height:42px"><span>Schedule a Consultation</span><span class="arrow"><svg width="16" height="16" viewBox="0 0 24 24"><path d="M4 12h15M13 6l6 6-6 6" stroke="#0b57a8" stroke-width="2.6" fill="none"/></svg></span></div>
</header>
<nav class="nav">
  <a>Home</a><a>About Us ⌄</a><a>Services ⌄</a><a>Portfolio</a><a>Blog</a><a>Contact Us</a>
</nav>

<!-- Hero -->
<section class="hero">
  <div class="hero-visual" role="img" aria-label="Hands typing on a laptop with glowing security lock and data icons"></div>
  <div class="abs" style="left:0;top:0;width:700px;height:560px;background:linear-gradient(90deg,var(--hero-a) 60%,rgba(31,58,69,0))"></div>
  <p class="kicker">Quorvalent – A Subsidiary Of Ardelle &amp; Co.</p>
  <h1>Our Vision is To Provide Ubiquitous ADA Compliant Web Technologies To Shift</h1>
  <p class="tag">Humanity Forward</p>
  <div class="btn" style="left:140px;top:352px;width:214px;height:42px;font-size:12.5px"><span>Schedule a Consultation</span><span class="arrow"><svg width="16" height="16" viewBox="0 0 24 24"><path d="M4 12h15M13 6l6 6-6 6" stroke="#0b57a8" stroke-width="2.6" fill="none"/></svg></span></div>
  <svg class="abs" style="left:0;top:400px" width="1200" height="160" viewBox="0 0 1200 160" preserveAspectRatio="none"><path d="M0 120 C90 190 250 150 400 90 C560 30 720 20 850 50 C980 80 1080 70 1200 40 L1200 160 L0 160Z" fill="#fff"/></svg>
</section>

<!-- Mission -->
<h2 class="title" style="top:800px"><span class="g">Our</span> Mission</h2>
<p class="p-center" style="top:857px">To increase awareness and opportunities in the personal &amp; professional lives of disabled persons through technology, regardless of gender, age race or socio-economic background.</p>
<div class="btn" style="left:531px;top:928px;width:138px;height:42px"><span>Contact Us</span><span class="arrow"><svg width="16" height="16" viewBox="0 0 24 24"><path d="M4 12h15M13 6l6 6-6 6" stroke="#0b57a8" stroke-width="2.6" fill="none"/></svg></span></div>

<!-- About -->
<div class="about-blob"></div>
<div class="about-img" role="img" aria-label="Two colleagues reviewing work together at a computer in an office"></div>
<h2 class="abs" style="left:608px;top:1106px;font-size:36px;font-weight:500;color:var(--blue)"><span class="g">About</span> Us</h2>
<p class="about-text" style="top:1163px">Quorvalent is a web based Internet and technology agency aimed at serving, educating, and partnering with brands &amp; organizations on how their products and services can advance the disabled community through inclusion and diversity.</p>
<p class="about-text" style="top:1275px">By integrating strategies, solutions, and practices accommodating all persons, we strive to shift humanity forward with the power of technology.</p>
<div class="btn" style="left:608px;top:1371px;width:140px;height:42px"><span>Contact Us</span><span class="arrow"><svg width="16" height="16" viewBox="0 0 24 24"><path d="M4 12h15M13 6l6 6-6 6" stroke="#0b57a8" stroke-width="2.6" fill="none"/></svg></span></div>

<!-- Services -->
<h2 class="title" style="top:1550px"><span class="g">Our</span> Services</h2>
<article class="card" style="left:140px">
  <div class="icon"><svg width="40" height="40" viewBox="0 0 40 40" fill="none" stroke="#333" stroke-width="2"><rect x="10" y="18" width="20" height="16" rx="2"/><path d="M14 18v-5a6 6 0 0 1 12 0v5"/><circle cx="20" cy="26" r="2.5"/></svg></div>
  <h3>Enhancing Website And<br>App Accessibility</h3>
  <p>Lorem ipsum dolor sit amet, consectetur adipiscing elit. Sed ante quam, imperdiet nec viverra vel, volutpat vel ex.</p>
  <div class="more">Read More →</div>
</article>
<article class="card" style="left:455px">
  <div class="icon"><svg width="40" height="40" viewBox="0 0 40 40" fill="none" stroke="#333" stroke-width="2"><circle cx="12" cy="12" r="4"/><circle cx="28" cy="12" r="4"/><path d="M5 32v-7a7 7 0 0 1 14 0v7M21 32v-7a7 7 0 0 1 14 0v7"/></svg></div>
  <h3>Adhering To<br>WCAG Guidelines</h3>
  <p>Lorem ipsum dolor sit amet, consectetur adipiscing elit. Sed ante quam, imperdiet nec viverra vel, volutpat vel ex.</p>
  <div class="more">Read More →</div>
</article>
<article class="card" style="left:770px">
  <div class="icon"><svg width="40" height="40" viewBox="0 0 40 40" fill="none" stroke="#333" stroke-width="2"><rect x="11" y="5" width="18" height="30" rx="3"/><circle cx="20" cy="15" r="4"/><path d="M16 30h8"/></svg></div>
  <h3>User-friendly Design<br>Consultations</h3>
  <p>Lorem ipsum dolor sit amet, consectetur adipiscing elit. Sed ante quam, imperdiet nec viverra vel, volutpat vel ex.</p>
  <div class="more">Read More →</div>
</article>

<!-- Client Reviews -->
<h2 class="abs" style="left:140px;top:2128px;font-size:36px;font-weight:500;color:var(--blue)"><span class="g">Client</span> Reviews</h2>
<p class="abs" style="left:140px;top:2180px;width:430px;font-size:13.5px;line-height:1.9;color:var(--muted)">Lorem ipsum dolor sit amet, consectetur adipiscing elit. Sed ante quam, imperdiet nec viverra vel, volutpat vel ex. Quisque lectus orci, blandit at accumsan eget, dignissim ac turpis. Fusce ornare orci eros, vitae rhoncus magna faucibus vitae. Nunc aliquam dapibus elit vel fringilla.</p>
<div class="btn" style="left:140px;top:2337px;width:140px;height:42px"><span>Read More</span><span class="arrow"><svg width="16" height="16" viewBox="0 0 24 24"><path d="M4 12h15M13 6l6 6-6 6" stroke="#0b57a8" stroke-width="2.6" fill="none"/></svg></span></div>
<div class="client" style="left:664px;top:2025px;color:var(--blue)"><span class="mark" style="background:var(--blue)"></span>YOUR COMPANY NAME</div>
<div class="client" style="left:858px;top:2103px;color:#d6336c"><span class="mark" style="background:#d6336c"></span>YOUR COMPANY NAME</div>
<div class="client" style="left:689px;top:2243px;color:#2e8b3a;font-size:16px"><span class="mark" style="background:#2e8b3a"></span>COMPANY</div>

<!-- Who we serve -->
<section class="serve">
  <div class="serve-visual" role="img" aria-label="Night city skyline with glowing network connection lines"></div>
  <svg class="abs" style="left:420px;top:0" width="60" height="273" viewBox="0 0 60 273"><path d="M0 0 H25 C5 90 60 180 40 273 H0Z" fill="#8dc63f"/></svg>
  <h2 class="abs" style="left:52px;top:30px;font-size:25px;font-weight:500;color:#111">Who does Quorvalent Serve?</h2>
  <p class="abs" style="left:54px;top:80px;width:370px;font-size:13px;line-height:1.95;color:#222">Who does Quorvalent serve? A person regardless of legal or medical mandates with a physical and/or mental ailment that prevents them from using technology without the use of an assistive software.</p>
  <div class="btn light" style="left:52px;top:190px;width:138px;height:42px"><span>Read More</span><span class="arrow"><svg width="16" height="16" viewBox="0 0 24 24"><path d="M4 12h15M13 6l6 6-6 6" stroke="#fff" stroke-width="2.6" fill="none"/></svg></span></div>
</section>

<!-- Blog -->
<h2 class="title" style="top:2875px"><span class="g">Latest</span> Blog Posts</h2>
<div class="side-arrow" style="left:72px;border:1.5px solid #aaa"><svg width="18" height="18" viewBox="0 0 24 24"><path d="M20 12H5M11 6l-6 6 6 6" stroke="#999" stroke-width="2.2" fill="none"/></svg></div>
<div class="side-arrow" style="left:1083px;border:2px solid var(--blue)"><svg width="18" height="18" viewBox="0 0 24 24"><path d="M4 12h15M13 6l6 6-6 6" stroke="#0b57a8" stroke-width="2.4" fill="none"/></svg></div>

<article class="post" style="left:140px">
  <div class="thumb" role="img" aria-label="Talk show title graphic in red and blue" style="background:linear-gradient(180deg,#8a1020,#1c3a9a 60%,#d0d4e8)"></div>
  <div class="date"><b>23</b>March</div>
  <h4>Living for Vision with Dalia Worth &amp; Renna Castell</h4>
  <p>Do you know what it means to have a vision for your life? Renna Castell, CEO of Quorvalent &amp; ArdelleCo, breaks it all down on...</p>
  <div class="more">Read More →</div>
</article>
<article class="post" style="left:458px">
  <div class="thumb" style="background:#3a3a3a;color:#fff">
    <div class="abs" style="left:24px;top:96px;font-size:16px;line-height:1.35">NFNA Food &amp; Nutrition Service<br>Interview with Marisol</div>
  </div>
  <div class="date"><b>19</b>March</div>
  <h4>Renna Castell Discusses Overcoming The Emotional And Psychologic</h4>
  <p>Renna Castell, chief experience officer for ArdelleCo &amp; Quorvalent discusses overcoming the emotional and psychological...</p>
  <div class="more">Read More →</div>
</article>
<article class="post" style="left:776px">
  <div class="thumb" role="img" aria-label="Hand reaching toward a glowing ring light in a red room" style="background:radial-gradient(circle at 55% 35%,#ffb08a,#e2452a 45%,#7a1a10)"></div>
  <div class="date"><b>26</b>March</div>
  <h4>Renna Castell Discusses Overcoming The Emotional And Psychologic</h4>
  <p>Renna Castell, chief experience officer for ArdelleCo &amp; Quorvalent discusses overcoming the emotional and psychological...</p>
  <div class="more">Read More →</div>
</article>
<div class="btn" style="left:527px;top:3340px;width:146px;height:42px;font-size:12.5px"><span>View All Posts</span><span class="arrow"><svg width="16" height="16" viewBox="0 0 24 24"><path d="M4 12h15M13 6l6 6-6 6" stroke="#0b57a8" stroke-width="2.6" fill="none"/></svg></span></div>

<!-- Newsletter -->
<div class="grey-band"></div>
<section class="news">
  <h2 style="font-size:35px;font-weight:500;margin-top:33px">Newsletter Sign Up</h2>
  <p style="font-size:12.5px;line-height:1.8;width:600px;margin:14px auto 0">Lorem ipsum dolor sit am Lorem ipsum dolor sit amet consectetur adipiscing elit. Donec mattis iaculis...et consectetur adipiscing elit. Donec mattis iaculis</p>
</section>
<div class="field" style="left:317px">Name</div>
<div class="field" style="left:530px">Email Address</div>
<div class="btn light" style="left:745px;top:3620px;width:138px;height:40px;font-size:12.5px"><span>Subscribe</span><span class="arrow" style="width:32px;height:32px"><svg width="15" height="15" viewBox="0 0 24 24"><path d="M4 12h15M13 6l6 6-6 6" stroke="#fff" stroke-width="2.6" fill="none"/></svg></span></div>

<!-- Footer -->
<footer>
  <div class="abs logo-word" style="left:140px;top:3785px;font-size:32px">QUORVALENT<span class="dot"></span></div>
  <div class="abs" style="left:140px;top:3840px;font-size:16px">(240) QUORVA - 9</div>

  <div class="fhead" style="left:485px"><span class="g">Quick</span> Links</div>
  <div class="flist" style="left:485px;top:3780px">• Home<br>• About Us<br>• Services<br>• Portfolio<br>• Blog<br>• Contact Us</div>

  <div class="fhead" style="left:671px"><span class="g">Contact</span> Details</div>
  <div class="frow" style="left:671px;top:3782px"><span class="fic"><svg width="13" height="13" viewBox="0 0 24 24"><path d="M12 2a7 7 0 0 0-7 7c0 5 7 13 7 13s7-8 7-13a7 7 0 0 0-7-7z" fill="none" stroke="#0b57a8" stroke-width="2.2"/><circle cx="12" cy="9" r="2.5" fill="#0b57a8"/></svg></span><span>123 Building Name, Street,<br>Dallas, Texas</span></div>
  <div class="frow" style="left:671px;top:3835px;align-items:center"><span class="fic"><svg width="12" height="12" viewBox="0 0 24 24"><path fill="#0b57a8" d="M6.6 10.8a15 15 0 0 0 6.6 6.6l2.2-2.2a1 1 0 0 1 1-.25 11 11 0 0 0 3.6.6 1 1 0 0 1 1 1V20a1 1 0 0 1-1 1A17 17 0 0 1 3 4a1 1 0 0 1 1-1h3.5a1 1 0 0 1 1 1c0 1.25.2 2.45.6 3.6a1 1 0 0 1-.25 1z"/></svg></span><span style="font-size:14px">123 456 7890</span></div>
  <div class="frow" style="left:671px;top:3873px;align-items:center"><span class="fic"><svg width="13" height="13" viewBox="0 0 24 24"><rect x="3" y="5" width="18" height="14" fill="none" stroke="#0b57a8" stroke-width="2.2"/><path d="M3 6l9 7 9-7" fill="none" stroke="#0b57a8" stroke-width="2.2"/></svg></span><span>inquiry@quorvalent.com</span></div>

  <div class="fhead" style="left:962px"><span class="g">Follow</span> Us</div>
  <div class="frow" style="left:962px;top:3782px;align-items:center"><span class="fic"></span><span>Faceboard</span></div>
  <div class="frow" style="left:962px;top:3817px;align-items:center"><span class="fic"></span><span>Snapframe</span></div>
  <div class="frow" style="left:962px;top:3852px;align-items:center"><span class="fic"></span><span>Linkwork</span></div>
</footer>
<div class="bottom"><span>© 2023 Quorvalent - All Rights Reserved.</span><span>Without a vision the people will perish. Pr 29:18</span></div>

</body>
</html>
```